Website Homepage Design

Daltrove Care Partners Inc. is a Canadian financial services company that specialize in the delivery and administration of alternative health benefit solutions. Daltrove is seeking to adjust their brand and develop a new website.

We like the design and layout of the website below but are not looking for an exact replica (be creative):

http://www.quellaretreat.example/

We want the colour scheme to be clean white and "fresh green", possibly with orange accents (links).

This posting is only for a website homepage design (no coding), but anyone who includes a new logo, in addition to the design, will get priority.

Best of luck,

Oliver
Updates

Project is guaranteed.

Please let me know if you are currently working on a design.

Thank you,

Oliver

*Update:

Two example websites with good colour scheme/design:

- http://budlynest.example/
- http://www.petalkinderhaus.example.au/

I have attached a wireframe and colour scheme to the project brief. The main colour should be the green one. Other colours can be used for highlights and accents, etc.

Target Market(s)

Business owners age 50+

Industry/Entity Type

Financial

Requirements
Must have
• - Clear and simple design
- Area for video (similar to http://www.quellaretreat.example)
Should not have
• - Lots of pictures

```html
<!DOCTYPE html>
<html lang="en">
<head>
<meta charset="utf-8">
<title>Daltrove Care Partners Inc. — Home</title>
<link href="https://fonts.googleapis.com/css2?family=Arimo:wght@400;700&display=swap" rel="stylesheet">
<style>
  :root {
    --backdrop: #ccfccc;
    --page: #ffffff;
    --green-deep: #0a6e0a;
    --green-mid: #3aa83a;
    --green-bright: #66cc66;
    --green-soft: #9ccc98;
    --green-text: #0f6b1a;
    --green-muted: #7ab87a;
    --accent: #f5c000;
    --video: #000000;
    --tab: #5c8f5c;
    --photo-green: #8cc874;
    --photo-stone: #7f8a7f;
    --leaf: #8fd072;
  }
  * { box-sizing: border-box; margin: 0; padding: 0; }
  html, body { width: 1200px; height: 1152px; overflow: hidden; background: var(--backdrop); }
  body { font-family: "Arimo", Arial, sans-serif; }
  .stage { position: absolute; left: 0; top: 0; width: 1024px; height: 983px; transform: scale(1.171875); transform-origin: 0 0; }
  .abs { position: absolute; }
  .page { left: 104px; top: 28px; width: 816px; height: 937px; background: var(--page); }

  .search-label { left: 690px; top: 42px; font-size: 11px; color: var(--green-mid); }
  .search-box { left: 741px; top: 34px; width: 174px; height: 20px; background: var(--green-soft); }
  .search-box svg { position: absolute; left: 6px; top: 3px; }

  .header-band { left: 250px; top: 58px; width: 665px; height: 34px; background: var(--green-soft); }
  .logo-block { left: 110px; top: 58px; width: 160px; height: 46px; background: linear-gradient(90deg, var(--green-deep), var(--green-mid)); clip-path: polygon(0 0, 88% 0, 100% 100%, 0 100%); }
  .logo { left: 142px; top: 66px; font-size: 24px; color: #fff; font-weight: 400; letter-spacing: 0.5px; }
  .nav { left: 260px; top: 79px; width: 613px; height: 24px; border-radius: 0 12px 12px 0; background: linear-gradient(180deg, #4cba4c, var(--green-deep)); }
  .nav a { color: #fff; text-decoration: none; font-size: 14px; position: absolute; top: 4px; }

  .greens { left: 110px; top: 58px; }
  .side-menu a { position: absolute; left: 130px; width: 128px; height: 21px; border-radius: 0 10px 10px 0; background: var(--green-soft); color: var(--green-text); font-size: 11px; line-height: 21px; padding-left: 8px; text-decoration: none; }

  .title { left: 314px; top: 113px; font-size: 14px; font-weight: 400; color: var(--green-text); }
  .tagline { left: 315px; top: 130px; font-size: 12.5px; color: var(--green-bright); }

  .photo-placeholder { left: 635px; top: 195px; width: 270px; height: 175px; background: linear-gradient(180deg, var(--photo-green), var(--photo-stone)); }
  .leaf-placeholder { left: 540px; top: 306px; width: 62px; height: 34px; background: var(--leaf); }
  .turf-placeholder { top: 600px; height: 70px; background: linear-gradient(180deg, rgba(156,204,152,0), #5fae3a 60%, #3f8f28); }

  .video-frame { left: 288px; top: 388px; width: 450px; height: 282px; background: #fff; }
  .video { left: 294px; top: 393px; width: 438px; height: 255px; background: var(--video); }
  .video-controls { left: 493px; top: 499px; width: 39px; height: 18px; border-radius: 9px; background: var(--green-soft); }
  .video-controls svg { position: absolute; left: 0; top: 0; }
  .tab { top: 638px; width: 67px; height: 13px; border-radius: 7px 7px 0 0; background: var(--tab); color: #e8f5e8; font-size: 7.5px; text-align: center; line-height: 13px; }
  .cta { top: 655px; height: 14px; background: linear-gradient(180deg, #6fd06f, #1e8a1e); color: #fff; font-size: 7px; font-weight: 700; text-align: center; line-height: 14px; }
  .cta.left { left: 338px; width: 173px; border-radius: 7px 0 0 7px; }
  .cta.right { left: 514px; width: 174px; border-radius: 0 7px 7px 0; }

  .link-col { top: 681px; }
  .link-col h3 { font-size: 14px; font-weight: 700; color: var(--accent); margin-bottom: 5px; }
  .link-col a { display: block; font-size: 11px; color: var(--green-text); text-decoration: none; line-height: 18.7px; }

  .news-panel { left: 110px; top: 811px; width: 805px; height: 95px; background: var(--green-soft); }
  .news-bar { left: 110px; top: 803px; width: 766px; height: 24px; border-radius: 0 12px 12px 0; background: var(--green-bright); box-shadow: 3px 2px 0 #fff; }
  .news-bar h2 { font-size: 14px; font-weight: 400; color: var(--green-text); padding-left: 23px; line-height: 22px; }
  .news-item { top: 833px; width: 140px; }
  .news-item time { display: block; font-size: 11px; color: var(--green-text); margin-bottom: 7px; }
  .news-item p { font-size: 10.5px; color: var(--green-muted); line-height: 12px; }

  .footer { left: 110px; top: 911px; width: 805px; height: 46px; background: linear-gradient(90deg, var(--green-deep), var(--green-mid) 60%, var(--green-bright)); color: #fff; font-size: 12px; text-align: center; padding-top: 26px; }
</style>
</head>
<body>
<div class="stage">
  <div class="abs page"></div>

  <span class="abs search-label">Search</span>
  <div class="abs search-box">
    <svg width="14" height="14" viewBox="0 0 14 14"><circle cx="5" cy="5" r="3.5" fill="none" stroke="#fff" stroke-width="1.6"/><line x1="7.5" y1="7.5" x2="12" y2="12" stroke="#fff" stroke-width="2"/></svg>
  </div>

  <div class="abs header-band"></div>
  <nav class="abs nav">
    <a style="left:40px">Products</a>
    <a style="left:162px">Education</a>
    <a style="left:290px">Clients</a>
    <a style="left:396px">Company</a>
    <a style="left:521px">Support</a>
  </nav>
  <div class="abs logo-block"></div>
  <div class="abs logo">Daltrove</div>

  <svg class="abs greens" width="805" height="612" viewBox="0 0 805 612">
    <defs>
      <linearGradient id="sideGrad" x1="0" y1="0" x2="1" y2="0">
        <stop offset="0" stop-color="#0a6e0a"/>
        <stop offset="1" stop-color="#4cba4c"/>
      </linearGradient>
    </defs>
    <path d="M0,335 C100,280 200,262 330,268 C450,275 550,320 650,315 C720,312 770,292 805,285 L805,612 L0,612 Z" fill="#9ccc98"/>
    <path d="M0,47 L172,47 C195,100 190,160 165,210 C150,240 148,258 155,268 C100,272 40,300 0,330 Z" fill="url(#sideGrad)"/>
    <path d="M0,352 C100,300 200,282 330,284 C450,287 560,318 650,318 C720,318 770,300 805,294" fill="none" stroke="#ffffff" stroke-width="3"/>
    <path d="M0,358 C100,306 200,288 330,290 C450,293 560,324 650,324 C720,324 770,306 805,300" fill="none" stroke="#f5c000" stroke-width="2"/>
  </svg>

  <nav class="side-menu">
    <a style="top:122px">About us</a>
    <a style="top:148px">Meet the Team</a>
    <a style="top:174px">News</a>
    <a style="top:200px">Careers</a>
    <a style="top:226px">Contact us</a>
  </nav>

  <h1 class="abs title">Daltrove Care Partners Inc.</h1>
  <p class="abs tagline">Company that specialize in the delivery and administration of alternative health benefit solutions.</p>

  <div class="abs photo-placeholder" role="img" aria-label="Photo: tuft of fresh grass growing from smooth black stones"></div>
  <div class="abs leaf-placeholder" role="img" aria-label="Photo: single green leaf"></div>
  <div class="abs turf-placeholder" style="left:110px; width:178px" role="img" aria-label="Photo: strip of green lawn"></div>
  <div class="abs turf-placeholder" style="left:738px; width:177px" role="img" aria-label="Photo: strip of green lawn"></div>

  <div class="abs video-frame"></div>
  <div class="abs video" role="img" aria-label="Video player"></div>
  <div class="abs video-controls">
    <svg width="39" height="18" viewBox="0 0 39 18">
      <line x1="19.5" y1="1" x2="19.5" y2="17" stroke="#fff" stroke-width="1"/>
      <path d="M8,5 L14,9 L8,13 Z" fill="#f08a20"/>
      <path d="M24,7 L26,7 L29,4.5 L29,13.5 L26,11 L24,11 Z" fill="#f08a20"/>
      <path d="M31,6 Q33,9 31,12" stroke="#f08a20" fill="none" stroke-width="1"/>
    </svg>
  </div>
  <div class="abs tab" style="left:444px">Why Daltrove</div>
  <div class="abs tab" style="left:514px">Any Time</div>
  <div class="abs cta left">View our Products and Prices</div>
  <div class="abs cta right">Get Started</div>

  <div class="abs link-col" style="left:133px">
    <h3>What we are.</h3>
    <a>About us.</a><a>Meet the Team</a><a>News</a><a>Careers</a>
  </div>
  <div class="abs link-col" style="left:272px">
    <h3>Let &nbsp;us help</h3>
    <a>Trening</a><a>Tech Support</a><a>Contact us</a><a>Help Suite</a><a>Data Conversions</a>
  </div>
  <div class="abs link-col" style="left:434px">
    <h3>Client</h3>
    <a>Client Finder</a><a>Success Stories</a><a>Refer a Business</a>
  </div>
  <div class="abs link-col" style="left:590px">
    <h3>Education</h3>
    <a>Daltrove University</a><a>Business Consulting</a><a>Webinars</a><a>White Papers</a>
  </div>
  <div class="abs link-col" style="left:769px">
    <h3>Cool Stuff</h3>
    <a>Demo Site</a><a>Blog</a><a>Videos</a><a>Results Calculator</a>
  </div>

  <div class="abs news-panel"></div>
  <div class="abs news-bar"><h2>Latest &nbsp;news</h2></div>
  <article class="abs news-item" style="left:133px">
    <time>April 20, 2011.</time>
    <p>Company that specialize in the delivery and administration ...</p>
  </article>
  <article class="abs news-item" style="left:340px; width:180px">
    <time>March 23, 2011...</time>
    <p>Company that specialize in<br>the delivery and administration ...</p>
  </article>
  <article class="abs news-item" style="left:561px">
    <time>May 3, 2011...</time>
    <p>Company thatspecialize in the delivery<br>and administration ...</p>
  </article>
  <article class="abs news-item" style="left:766px">
    <time>May 28, 2011...</time>
    <p>Company that specialize in the delivery and...</p>
  </article>

  <footer class="abs footer">Copyright</footer>
</div>
</body>
</html>
```